Video production company website

VistaKeel Productions is a video and photography production company serving many Fortune 500 clients traveling to Hawaii and International Destinations. Our primary focus is the Corporate and Incentive group market, and offer both photography and video services. In addition, we also create custom marketing, sales, art, and real estate productions.

Target Market(s)

Corporate Incentive Travel Groups

Industry/Entity Type

Videography

Number of Pages Required

4 page

Requirements
Must have
• see doc with content. This will ultimately be needed to be a wordpress design so we can update ourselves.
Nice to have
• sleek design, professional, cutting edge, modern
Should not have
• too much Hawaii Feel, some ok but we do travel international

```html
<!DOCTYPE html>
<html lang="en">
<head>
<meta charset="utf-8">
<title>VistaKeel Productions</title>
<link href="https://fonts.googleapis.com/css2?family=Lato:wght@400;700&family=Ubuntu:wght@400;500;700&display=swap" rel="stylesheet">
<style>
:root{
  --blue:#1f7fcf;
  --blue-dark:#1a6cb0;
  --gold:#e3a425;
  --ink:#2b2b2b;
  --text:#444;
  --grey-band:#ececec;
  --card:#dedede;
  --white:#fff;
}
*{box-sizing:border-box;margin:0;padding:0}
html,body{width:1200px;height:3130px;overflow:hidden}
body{position:relative;font-family:'Lato',sans-serif;color:var(--text);background:var(--white)}
.abs{position:absolute}
h2.section-title{font-family:'Ubuntu',sans-serif;font-weight:700;font-size:30px;text-align:center;color:var(--blue);letter-spacing:.5px}
h2.section-title span{color:var(--gold)}
.title-rule{height:1px;background:#cfcfcf;width:320px;margin:12px auto 0}

/* top bar */
.topbar{left:0;top:0;width:1200px;height:38px;background:var(--ink)}
.topbar .social{position:absolute;top:10px;left:833px;display:flex;gap:6px}
.topbar .social i{display:block;width:19px;height:19px;border-radius:50%;background:#9a9a9a}
.topbar .phone{position:absolute;top:9px;left:975px;color:#fff;font-size:15px;display:flex;align-items:center;gap:8px}

/* header */
.brand{left:80px;top:46px;display:flex;align-items:center;gap:10px}
.brand .dot{width:40px;height:40px;border-radius:50%;background:var(--ink)}
.brand .name{font-family:'Ubuntu',sans-serif;font-weight:700;font-size:22px;color:var(--ink)}
.book-btn{left:877px;top:78px;height:38px;width:244px;border-radius:19px;background:var(--gold);color:#fff;font-family:'Ubuntu',sans-serif;font-weight:700;font-size:14px;display:flex;align-items:center;padding-left:62px}
.book-btn .ico{position:absolute;left:0;top:-3px;width:44px;height:44px;border-radius:50%;background:var(--blue);border:3px solid #fff;display:flex;align-items:center;justify-content:center}

/* nav */
.nav{left:0;top:155px;width:1200px;height:43px;background:var(--blue)}
.nav ul{list-style:none;position:relative;height:43px}
.nav li{position:absolute;top:0;height:43px;line-height:43px;font-family:'Ubuntu',sans-serif;font-weight:700;font-size:14px;color:#fff;text-align:center}
.nav li.active{background:var(--gold)}

/* hero */
.hero{left:0;top:198px;width:1200px;height:472px;background:linear-gradient(180deg,#9dc9e8 0%,#c7dce6 45%,#7a9a6a 70%,#4d6b3c 100%)}
.hero .caption{position:absolute;left:440px;top:615px;width:480px;height:50px}
.hero-caption{left:440px;top:612px;width:480px;height:52px;background:rgba(0,0,0,.35);color:#fff;font-family:'Ubuntu',sans-serif;font-weight:700;font-size:27px;text-align:center;line-height:52px}
.hero-arrow{top:386px;width:36px;height:36px;background:rgba(0,0,0,.55);display:flex;align-items:center;justify-content:center}

/* welcome */
.welcome-title{left:80px;top:744px;font-family:'Ubuntu',sans-serif;font-weight:700;font-size:29px;color:var(--blue)}
.welcome-title span{color:var(--gold)}
.welcome-title small{font-size:16px;color:var(--ink)}
.welcome-rule{left:80px;top:796px;width:625px;height:1px;background:#d6d6d6}
.welcome-copy{left:80px;top:808px;width:625px;font-size:14.5px;line-height:1.62;color:#3a3a3a}
.person{top:918px;display:flex;align-items:center;gap:14px}
.person .avatar{width:72px;height:72px;border-radius:50%;border:3px solid #e6e6e6;background:linear-gradient(135deg,#c9a07c,#7a5a3e)}
.person .pname{font-family:'Ubuntu',sans-serif;font-weight:500;font-size:20px;color:var(--blue)}
.person .prole{font-family:'Ubuntu',sans-serif;font-weight:500;font-size:14px;color:var(--ink);margin-top:2px}

.inquiry{left:762px;top:724px;width:357px;height:292px;border:1px solid #d3d3d3;background:#fff}
.inquiry-tab{left:762px;top:711px;width:315px;height:42px;background:#4a4a4a;color:#fff;font-family:'Ubuntu',sans-serif;font-weight:700;font-size:21px;text-align:center;line-height:42px;margin-left:21px}
.inquiry-tab span{color:var(--gold)}
.field{left:783px;width:315px;background:#ececec;border:1px solid #d0d0d0;border-radius:3px;font-size:13px;color:#666;padding:8px 8px}
.field b{color:#d33;font-weight:400}
.submit{left:783px;top:958px;width:129px;height:34px;background:var(--blue);color:#fff;font-family:'Ubuntu',sans-serif;font-weight:700;font-size:15px;text-align:center;line-height:34px}

/* services */
.services{left:0;top:1062px;width:1200px;height:514px;background:linear-gradient(180deg,#6e6a62 0%,#4a4740 35%,#2c2b28 70%,#1d1c1a 100%)}
.services h2.section-title{color:#fff;padding-top:43px}
.services .title-rule{background:#9a968d;width:330px}
.svc{width:260px;color:#fff}
.svc h3{font-family:'Ubuntu',sans-serif;font-weight:700;font-size:20px}
.svc p{font-size:13px;line-height:1.5;color:#d4d4d4;margin-top:2px}
.svc.left{text-align:right}
.svc-icon{width:56px;height:56px}
.center-mark{left:455px;top:1205px;width:290px;height:290px;border-radius:50%;border:14px solid #b8c6d2;background:radial-gradient(circle at 40% 35%,rgba(255,255,255,.18),rgba(0,0,0,.15));display:flex;align-items:center;justify-content:center;font-family:'Ubuntu',sans-serif;font-weight:700;font-size:38px;color:#e8edf2}

/* gallery */
.gallery-title{left:0;top:1602px;width:1200px}
.filter{top:1673px;left:388px;display:flex;align-items:center;gap:8px;font-family:'Ubuntu',sans-serif;font-size:14px;color:var(--ink)}
.filter .lbl{margin-right:14px}
.filter .btn{height:44px;line-height:42px;padding:0 16px;border:1px solid #bdbdbd;font-size:14px}
.filter .btn.on{background:var(--gold);border-color:var(--gold);color:#fff;font-weight:700;padding:0 22px}
.tile{overflow:hidden}
.play{position:absolute;left:50%;top:50%;transform:translate(-50%,-50%);background:rgba(0,0,0,.75);border-radius:14px;display:flex;align-items:center;justify-content:center}
.hover-box{left:359px;top:1746px;width:480px;height:108px;border:1px solid rgba(255,255,255,.55);color:#fff;text-align:center}
.hover-box h4{font-family:'Ubuntu',sans-serif;font-weight:700;font-size:16px;margin-top:12px}
.hover-box p{font-size:13px;line-height:1.5;margin:8px 60px 0}
.pager{top:2297px;left:576px;display:flex;gap:3px}
.pager i{display:flex;width:22px;height:22px;align-items:center;justify-content:center}

/* testimonials */
.testimonials{left:0;top:2371px;width:1200px;height:409px;background:var(--grey-band)}
.testimonials h2.section-title{padding-top:52px}
.quote-card{top:2515px;width:512px;height:146px;background:var(--card);border-radius:4px;padding:18px 120px 0 18px}
.quote-card h5{font-family:'Ubuntu',sans-serif;font-weight:500;font-size:15px;color:var(--blue)}
.quote-card p{font-size:13.5px;line-height:1.5;color:#333;margin-top:6px}
.quote-card .tail{position:absolute;left:46px;bottom:-30px;width:0;height:0;border-left:0 solid transparent;border-right:50px solid transparent;border-top:30px solid var(--card)}
.quote-mark{position:absolute;right:22px;top:14px}
.t-avatar{width:98px;height:98px;border-radius:50%;border:4px solid #fff;background:linear-gradient(135deg,#e3c4a6,#8a6a4e)}
.t-name{font-family:'Ubuntu',sans-serif;font-weight:500;font-size:15px;color:#333}
.t-name .stars{color:var(--gold);letter-spacing:2px;margin-left:6px}
.t-arrow{top:2562px;width:36px;height:36px;border-radius:50%;background:#fff;border:1px solid #ccc;display:flex;align-items:center;justify-content:center}

/* footer */
.footer{left:0;top:2780px;width:1200px;height:296px;background:var(--blue)}
.f-head{top:2822px;font-family:'Ubuntu',sans-serif;font-weight:700;font-size:14px;color:#fff}
.f-links{left:80px;top:2863px;list-style:none;font-size:13.5px;color:#fff;line-height:25px}
.f-links li::before{content:"›";color:var(--gold);font-weight:700;margin-right:7px}
.f-contact{left:292px;font-size:13px;color:#fff;display:flex;gap:12px;align-items:flex-start;line-height:1.4}
.f-map{left:616px;top:2870px;width:234px;height:140px;border:3px solid #fff;background:linear-gradient(135deg,#dfe8d8,#c8d8e6 55%,#b3cfe8)}
.f-social{left:956px;top:2872px;display:flex;gap:10px}
.f-social i{display:block;width:32px;height:32px;border-radius:50%;background:var(--gold)}
.f-social i:first-child{background:#fff}
.f-mark{left:988px;top:2920px;width:96px;height:96px;border-radius:50%;border:4px solid rgba(255,255,255,.45);display:flex;align-items:center;justify-content:center;font-family:'Ubuntu',sans-serif;font-weight:700;font-size:15px;color:rgba(255,255,255,.55)}
.copyright{left:0;top:3076px;width:1200px;height:54px;background:#d9a31f;color:#fff;font-size:13.5px;text-align:center;line-height:54px}
</style>
</head>
<body>

<!-- top bar -->
<div class="abs topbar">
  <div class="social"><i></i><i></i><i></i><i></i></div>
  <div class="phone">
    <svg width="14" height="14" viewBox="0 0 24 24"><path fill="#fff" d="M6.6 10.8a15.1 15.1 0 0 0 6.6 6.6l2.2-2.2c.3-.3.7-.4 1-.2 1.1.4 2.3.6 3.6.6.6 0 1 .4 1 1V20c0 .6-.4 1-1 1A17 17 0 0 1 3 4c0-.6.4-1 1-1h3.5c.6 0 1 .4 1 1 0 1.3.2 2.5.6 3.6.1.3 0 .7-.2 1z"/></svg>
    (123) 555.0142
  </div>
</div>

<!-- header -->
<div class="abs brand"><span class="dot"></span><span class="name">VistaKeel Productions</span></div>
<div class="abs book-btn">
  <span class="ico"><svg width="20" height="20" viewBox="0 0 24 24"><rect x="3" y="5" width="18" height="16" rx="2" fill="none" stroke="#fff" stroke-width="2"/><path d="M3 10h18M8 3v4M16 3v4" stroke="#fff" stroke-width="2"/></svg></span>
  BOOK YOUR SERVICE
</div>

<nav class="abs nav">
  <ul>
    <li class="active" style="left:80px;width:95px">HOME</li>
    <li style="left:190px;width:105px">ABOUT US</li>
    <li style="left:318px;width:130px">VIDEOGRAPHY</li>
    <li style="left:478px;width:145px">PHOTOGRAPHY</li>
    <li style="left:650px;width:160px">WHY CHOOSE US</li>
    <li style="left:825px;width:140px">TESTIMONIALS</li>
    <li style="left:990px;width:130px">CONTACT US</li>
  </ul>
</nav>

<!-- hero -->
<div class="abs hero" role="img" aria-label="Camera operator filming a smiling couple on a tropical lawn by the sea with palm trees"></div>
<div class="abs hero-caption">The Best of the Best</div>
<div class="abs hero-arrow" style="left:4px"><svg width="12" height="14" viewBox="0 0 12 14"><path d="M9 1 3 7l6 6" fill="none" stroke="#fff" stroke-width="2.5"/></svg></div>
<div class="abs hero-arrow" style="left:1160px"><svg width="12" height="14" viewBox="0 0 12 14"><path d="m3 1 6 6-6 6" fill="none" stroke="#fff" stroke-width="2.5"/></svg></div>

<!-- welcome -->
<h1 class="abs welcome-title">WELCOME TO VISTAKEEL <span>PRODUCTIONS</span> <small>LLC</small></h1>
<div class="abs welcome-rule"></div>
<p class="abs welcome-copy">VistaKeel Productions is a video and photography production company serving many Fortune 500 clients in Hawaii and Internationally. Our primary focus is the Corporate and Incentive group market, and offer both photography and video services. In addition, we also create custom marketing, sales, art, and real estate productions.</p>
<div class="abs person" style="left:80px">
  <div class="avatar" role="img" aria-label="Portrait of the owner"></div>
  <div><div class="pname">Martin Okafor</div><div class="prole">Owner and Producer</div></div>
</div>
<div class="abs person" style="left:370px">
  <div class="avatar" role="img" aria-label="Portrait of the producer"></div>
  <div><div class="pname">Lena Voss</div><div class="prole">Producer</div></div>
</div>

<div class="abs inquiry"></div>
<div class="abs inquiry-tab">QUICK <span>INQUIRY</span></div>
<div class="abs field" style="top:776px;height:34px">Name <b>*</b></div>
<div class="abs field" style="top:818px;height:34px">Email <b>*</b></div>
<div class="abs field" style="top:860px;height:80px">Message <b>*</b></div>
<div class="abs submit">SUBMIT</div>

<!-- services -->
<section class="abs services" role="img" aria-label="Dusky ocean bay with mountain silhouettes behind">
  <h2 class="section-title">OUR <span>SERVICES</span></h2>
  <div class="title-rule"></div>
</section>
<svg class="abs" style="left:0;top:1062px" width="1200" height="514" viewBox="0 0 1200 514">
  <g stroke="#9c978c" stroke-width="1.5" fill="none">
    <path d="M380 162 H470 L500 200"/>
    <path d="M395 270 H460"/>
    <path d="M380 384 H470 L500 346"/>
    <path d="M820 162 H730 L700 200"/>
    <path d="M805 270 H740"/>
    <path d="M820 384 H730 L700 346"/>
  </g>
  <g fill="var(--gold)">
    <circle cx="380" cy="162" r="5"/><circle cx="395" cy="270" r="5"/><circle cx="380" cy="384" r="5"/>
    <circle cx="820" cy="162" r="5"/><circle cx="805" cy="270" r="5"/><circle cx="820" cy="384" r="5"/>
  </g>
</svg>
<div class="abs center-mark">VistaKeel</div>

<div class="abs svc left" style="left:55px;top:1206px"><h3>Videography</h3><p>Lorem ipsum dolor sit amet,<br>consectetuer Lorem ipsum dolo ...</p></div>
<svg class="abs svc-icon" style="left:318px;top:1206px" viewBox="0 0 56 56"><g fill="#fff"><circle cx="18" cy="14" r="7"/><circle cx="34" cy="14" r="7"/><rect x="10" y="23" width="28" height="18" rx="2"/><path d="M38 28l10-6v20l-10-6z"/><path d="M20 41l-6 10h4l5-8zM28 41l6 10h-4l-5-8z"/></g></svg>

<div class="abs svc left" style="left:55px;top:1320px"><h3>Real Estate Productions</h3><p>Lorem ipsum dolor sit amet,<br>consectetuer Lorem ipsum dolo ...</p></div>
<svg class="abs svc-icon" style="left:322px;top:1318px" viewBox="0 0 56 56"><g fill="none" stroke="#fff" stroke-width="4" stroke-linejoin="round"><path d="M6 26 28 8l22 18"/><path d="M13 22v18h30V22"/><path d="M22 40l6-10 6 10M14 52l6-12M42 52l-6-12"/></g></svg>

<div class="abs svc left" style="left:55px;top:1434px"><h3>Art</h3><p>Lorem ipsum dolor sit amet,<br>consectetuer Lorem ipsum dolo ...</p></div>
<svg class="abs svc-icon" style="left:322px;top:1430px" viewBox="0 0 56 56"><path fill="#fff" d="M28 6C14 6 4 16 4 28s10 22 22 22c4 0 5-3 3-6-2-3 0-6 4-6h6c8 0 13-5 13-12C52 14 41 6 28 6z"/><g fill="#3a3833"><circle cx="16" cy="26" r="4"/><circle cx="22" cy="16" r="4"/><circle cx="34" cy="15" r="4"/><circle cx="42" cy="24" r="4"/></g></svg>

<svg class="abs svc-icon" style="left:822px;top:1210px" viewBox="0 0 56 56"><g fill="#fff"><path d="M6 18h10l4-6h16l4 6h10v28H6z"/></g><circle cx="28" cy="31" r="9" fill="none" stroke="#3a3833" stroke-width="4"/></svg>
<div class="abs svc" style="left:883px;top:1212px"><h3>Photography</h3><p>Lorem ipsum dolor sit amet,<br>consectetuer Lorem ipsum dolo ...</p></div>

<svg class="abs svc-icon" style="left:818px;top:1320px" viewBox="0 0 56 56"><rect x="4" y="8" width="48" height="40" fill="none" stroke="#fff" stroke-width="4"/><path d="M4 16h48" stroke="#fff" stroke-width="4"/><path d="M22 24v16l14-8z" fill="#fff"/></svg>
<div class="abs svc" style="left:883px;top:1320px"><h3>Custom Marketing</h3><p>Lorem ipsum dolor sit amet,<br>consectetuer Lorem ipsum dolo ...</p></div>

<svg class="abs svc-icon" style="left:818px;top:1428px" viewBox="0 0 56 56"><g fill="#fff"><path d="M4 8h18l24 24-18 18L4 26z"/><path d="M26 6h4l22 22-14 14-2-2 12-12z"/></g><circle cx="13" cy="17" r="3.5" fill="#3a3833"/></svg>
<div class="abs svc" style="left:883px;top:1430px"><h3>Sales</h3><p>Lorem ipsum dolor sit amet,<br>consectetuer Lorem ipsum dolo ...</p></div>

<!-- gallery -->
<div class="abs gallery-title"><h2 class="section-title">OUR <span>GALLERY</span></h2><div class="title-rule"></div></div>
<div class="abs filter">
  <span class="lbl">FILTER</span>
  <span class="btn on">ALL</span>
  <span class="btn">PHOTOGRAPHY</span>
  <span class="btn">VIDEOGRAPHY</span>
</div>

<div class="abs tile" style="left:79px;top:1736px;width:267px;height:317px;background:linear-gradient(180deg,#a9c4b0,#6f8fa6 60%,#3f5f88)" role="img" aria-label="Banquet tables set outdoors beneath palms and hanging decorations"></div>
<div class="abs tile" style="left:351px;top:1736px;width:496px;height:151px;background:linear-gradient(180deg,#4a4238,#2d2822)" role="img" aria-label="Guest smiling at an evening event, shown under a dark overlay"></div>
<div class="abs hover-box">
  <h4>Lorem ipsum dolor sit amet</h4>
  <p>Lorem ipsum dolor sit amet, consectetuer adipiscing elit, sed diam nonummy sit amet, consectetuer adipiscing elit</p>
  <svg class="abs" style="left:229px;top:82px" width="22" height="22" viewBox="0 0 22 22"><circle cx="11" cy="11" r="9.5" fill="none" stroke="#fff" stroke-width="1.5"/><path d="M11 6v10M6 11h10" stroke="#fff" stroke-width="1.8"/></svg>
</div>
<div class="abs tile" style="left:851px;top:1736px;width:268px;height:317px;background:linear-gradient(180deg,#e9a23a 0%,#c96a2a 35%,#3e5c86 60%,#22304a)" role="img" aria-label="Candlelit dinner tables by the sea at sunset"></div>
<div class="abs tile" style="left:351px;top:1891px;width:248px;height:162px;background:linear-gradient(180deg,#5fc6cf,#1f8f9e)" role="img" aria-label="Person leaping into turquoise water">
  <span class="play" style="width:52px;height:36px"><svg width="14" height="16" viewBox="0 0 14 16"><path d="M1 1l12 7-12 7z" fill="#fff"/></svg></span>
</div>
<div class="abs tile" style="left:603px;top:1891px;width:244px;height:162px;background:linear-gradient(180deg,#3a1f1a,#6a3a2a 60%,#2a1a16)" role="img" aria-label="Three guests posing before a lit welcome sign at night"></div>
<div class="abs tile" style="left:79px;top:2060px;width:520px;height:215px;background:linear-gradient(180deg,#b7cde0 0%,#8fa88a 40%,#3f4a52 75%,#2c3138)" role="img" aria-label="Large corporate group photo on a lakeside terrace"></div>
<div class="abs tile" style="left:603px;top:2060px;width:516px;height:215px;background:linear-gradient(180deg,#8aa7b8,#b9c9cf 45%,#e4e6e2 70%,#a7b5b4)" role="img" aria-label="Child riding a surfboard in shallow waves">
  <span class="play" style="width:76px;height:52px"><svg width="20" height="22" viewBox="0 0 14 16"><path d="M1 1l12 7-12 7z" fill="#fff"/></svg></span>
</div>
<div class="abs pager">
  <i style="background:#bbb"><svg width="12" height="12" viewBox="0 0 12 12"><path d="M11 6H2M6 2 2 6l4 4" fill="none" stroke="#fff" stroke-width="2"/></svg></i>
  <i style="background:#1d2a4a"><svg width="12" height="12" viewBox="0 0 12 12"><path d="M1 6h9M6 2l4 4-4 4" fill="none" stroke="#fff" stroke-width="2"/></svg></i>
</div>

<!-- testimonials -->
<section class="abs testimonials">
  <h2 class="section-title">CLIENT <span>TESTIMONIALS</span></h2>
  <div class="title-rule"></div>
</section>
<div class="abs t-arrow" style="left:18px"><svg width="10" height="12" viewBox="0 0 10 12"><path d="M7 1 2 6l5 5" fill="none" stroke="#777" stroke-width="2"/></svg></div>
<div class="abs t-arrow" style="left:1142px"><svg width="10" height="12" viewBox="0 0 10 12"><path d="m3 1 5 5-5 5" fill="none" stroke="#777" stroke-width="2"/></svg></div>

<div class="abs quote-card" style="left:79px">
  <h5>Lorem ipsum dolor sit amet, consectet uer</h5>
  <p>Lorem ipsum dolor sit amet, consectet uer adipiscing elit, sed diam nonummy nibh euis mod tincidun nt ut laoreetml dolore magna aliquam erat volutpat.</p>
  <svg class="quote-mark" width="104" height="90" viewBox="0 0 104 90"><g fill="#fff"><path d="M4 0h40v46c0 24-14 40-36 44l-4-12c12-4 18-12 18-24H4z"/><path d="M60 0h40v46c0 24-14 40-36 44l-4-12c12-4 18-12 18-24H60z"/></g></svg>
  <span class="tail"></span>
</div>
<div class="abs t-avatar" style="left:103px;top:2625px" role="img" aria-label="Client portrait"></div>
<div class="abs t-name" style="left:300px;top:2682px">- Miss Tavia Renholm <span class="stars">★★★★★</span></div>

<div class="abs quote-card" style="left:611px">
  <h5>Lorem ipsum dolor sit amet, consectet uer</h5>
  <p>Lorem ipsum dolor sit amet, consectet uer adipiscing elit, sed diam nonummy nibh euis mod tincidun nt ut laoreetml dolore magna aliquam erat volutpat.</p>
  <svg class="quote-mark" width="104" height="90" viewBox="0 0 104 90"><g fill="#fff"><path d="M4 0h40v46c0 24-14 40-36 44l-4-12c12-4 18-12 18-24H4z"/><path d="M60 0h40v46c0 24-14 40-36 44l-4-12c12-4 18-12 18-24H60z"/></g></svg>
  <span class="tail"></span>
</div>
<div class="abs t-avatar" style="left:640px;top:2625px" role="img" aria-label="Client portrait"></div>
<div class="abs t-name" style="left:812px;top:2682px">Mr. Dorian Pell <span class="stars">★★★★★</span></div>

<!-- footer -->
<footer class="abs footer"></footer>
<div class="abs f-head" style="left:80px">QUICK LINKS</div>
<ul class="abs f-links">
  <li>Home</li><li>About Us</li><li>Videography</li><li>Photography</li><li>Why Choose Us</li><li>Testimonials</li><li>Contact Us</li>
</ul>

<div class="abs f-head" style="left:292px">CONTACT DETAILS</div>
<div class="abs f-contact" style="top:2866px">
  <svg width="14" height="20" viewBox="0 0 14 20"><path d="M7 0a7 7 0 0 0-7 7c0 5 7 13 7 13s7-8 7-13a7 7 0 0 0-7-7z" fill="var(--gold)"/><circle cx="7" cy="7" r="2.5" fill="var(--blue)"/></svg>
  <div><b>VistaKeel Productions, LLC</b><br><span style="font-size:12px">P.O. Box 410-227</span></div>
</div>
<div class="abs f-contact" style="top:2922px">
  <svg width="15" height="15" viewBox="0 0 24 24"><path fill="var(--gold)" d="M6.6 10.8a15.1 15.1 0 0 0 6.6 6.6l2.2-2.2c.3-.3.7-.4 1-.2 1.1.4 2.3.6 3.6.6.6 0 1 .4 1 1V20c0 .6-.4 1-1 1A17 17 0 0 1 3 4c0-.6.4-1 1-1h3.5c.6 0 1 .4 1 1 0 1.3.2 2.5.6 3.6.1.3 0 .7-.2 1z"/></svg>
  <div>(123) 555.0142</div>
</div>
<div class="abs f-contact" style="top:2958px">
  <svg width="16" height="15" viewBox="0 0 24 22"><rect x="1" y="6" width="22" height="15" rx="2" fill="var(--gold)"/><path d="M5 6V2h14v4" fill="none" stroke="var(--gold)" stroke-width="2.5"/><rect x="7" y="11" width="10" height="5" fill="var(--blue)"/></svg>
  <div>(123) 555.0142</div>
</div>
<div class="abs f-contact" style="top:2994px;font-size:12px">
  <svg width="15" height="11" viewBox="0 0 22 16"><rect width="22" height="16" rx="1" fill="var(--gold)"/><path d="M1 1l10 8 10-8" fill="none" stroke="var(--blue)" stroke-width="2"/></svg>
  <div>info@vistakeelproductions.com</div>
</div>

<div class="abs f-head" style="left:616px">LOCATION MAP</div>
<div class="abs f-map" role="img" aria-label="Street map showing the office location"></div>

<div class="abs f-head" style="left:956px">FOLLOW US</div>
<div class="abs f-social"><i></i><i></i><i></i><i></i></div>
<div class="abs f-mark">VistaKeel</div>

<div class="abs copyright">Copyright © 2016 VistaKeel Productions.&nbsp; All Rights Reserved.</div>

</body>
</html>
```